依頼概要
■依頼の目的/概要
インフルエンザワクチンのポスターを作成して頂きたいです。
クリニック内の待合室に掲示します。

■依頼詳細
A2サイズです。
温かみのある柔らかいデザインをお願いします。
ポスターには、人のイラスト入りでお願いします。イラストはご自身で書いてくださってもいいですし、フリー素材でも構いません。
色合いは当院ホームページを参考にしてください。
当院ホームページ https://temuzeku.com/

記載する内容については、添付ファイルを参照してください。
ロゴデータは当選決定後に送らせて頂きます。

納品は、元データ(aiファイルやpsdファイル)とPNG書き出しでお願いします。

■重視する点
過去・現在までにデザインの経験のある方を希望致します。

その他何かご不明な点がございましたら、お気軽にご質問下さい。
よろしくお願いいたします。

文字が大きく読みやすい、温かみのあるデザインです。

皆さま、この度は当コンペにご参加いただき、誠にありがとうございます。
どれも力作で魅力的で選ぶのが大変でした。
今後ともどうぞよろしくお願いします。

```html
<!DOCTYPE html>
<html lang="ja">
<head>
<meta charset="utf-8">
<title>インフルエンザ予防接種</title>
<link rel="stylesheet" href="https://fonts.googleapis.com/css2?family=M+PLUS+Rounded+1c:wght@500;700;800&display=swap">
<style>
:root{
  --green:#3f9a48;
  --green-dark:#2f7f38;
  --green-pale:#dff0d6;
  --bg:#cfe8c4;
  --red:#e2302a;
  --orange:#ef9a2b;
  --cream:#fdf4e6;
  --ink:#333;
  --white:#fff;
}
*{box-sizing:border-box;margin:0;padding:0}
html,body{width:849px;height:1200px;overflow:hidden}
body{background:var(--bg);font-family:"M PLUS Rounded 1c",sans-serif;color:var(--ink)}
.poster{position:absolute;left:24px;top:24px;width:801px;height:1152px;background:var(--white);border-radius:28px;overflow:hidden}
.title-small{position:absolute;left:60px;top:44px;font-size:58px;font-weight:800;color:var(--green);letter-spacing:2px;line-height:1.1}
.title-big{position:absolute;left:56px;top:112px;font-size:112px;font-weight:800;color:var(--green);letter-spacing:4px;line-height:1}
.date{position:absolute;left:56px;top:248px;font-size:64px;font-weight:800;color:var(--red);line-height:1}
.date .wd{display:inline-block;background:var(--red);color:var(--white);border-radius:50%;width:52px;height:52px;font-size:34px;text-align:center;line-height:52px;vertical-align:middle;margin:0 4px}
.start{position:absolute;left:56px;top:322px;font-size:58px;font-weight:800;color:var(--red);line-height:1}
.notice{position:absolute;left:56px;top:400px;width:430px;height:40px;background:var(--orange);color:var(--white);font-size:24px;font-weight:700;line-height:40px;padding-left:20px;border-radius:4px}
.doctor{position:absolute;right:34px;top:40px;width:220px;height:360px;border-radius:110px 110px 20px 20px;background:linear-gradient(#f3e3cf,#e9f3f6)}
.points{position:absolute;left:36px;top:460px;width:729px;height:236px;background:var(--cream);border-radius:14px;padding:14px 190px 0 24px}
.points li{list-style:none;position:relative;padding-left:22px;font-size:17px;font-weight:500;line-height:1.4;margin-bottom:3px}
.points li::before{content:"";position:absolute;left:0;top:6px;width:13px;height:13px;border-radius:50%;background:var(--orange)}
.couple{position:absolute;right:50px;top:520px;width:160px;height:140px;border-radius:70px;background:linear-gradient(#f6dcc2,#f3ecd8)}
.fees{position:absolute;left:36px;top:710px;width:729px;border-collapse:collapse;font-size:20px}
.fees th{background:var(--green);color:var(--white);font-weight:700;height:42px;border:2px solid var(--white)}
.fees td{border:2px solid var(--green);text-align:center;vertical-align:middle;padding:8px 6px;font-weight:700}
.fees .who{background:var(--green-pale);text-align:left;padding-left:16px;width:230px}
.who .main{color:var(--green-dark);font-size:26px;font-weight:800;display:block}
.who .sub{font-size:20px;display:block;margin-top:6px}
.who .tiny{font-size:11px;font-weight:500;display:block;line-height:1.4;margin-top:4px}
.who .other{color:var(--red);font-size:24px;font-weight:800;display:block}
.fee-city{color:var(--red);font-size:18px;display:block}
.fee-price{font-size:40px;font-weight:800;display:block;line-height:1.2}
.fee-price small{font-size:22px}
.fee-note{font-size:14px;font-weight:500;display:block}
.fee-count{font-size:14px;display:block}
.dose{display:flex;align-items:center;justify-content:center;gap:14px;font-size:36px;font-weight:800;margin:6px 0}
.dose span{background:var(--red);color:var(--white);font-size:16px;padding:3px 8px;border-radius:4px}
.dose.second span{background:var(--orange)}
.clinic{position:absolute;left:0;bottom:0;width:801px;height:96px;background:var(--green-pale);display:flex;align-items:center;padding-left:420px;gap:12px;color:var(--green-dark);font-size:32px;font-weight:800}
.clinic i{width:34px;height:34px;border-radius:50%;background:var(--green)}
</style>
</head>
<body>
<main class="poster">
  <p class="title-small">インフルエンザ</p>
  <h1 class="title-big">予防接種</h1>
  <p class="date">10月11日<span class="wd">金</span>から</p>
  <p class="start">始まります。</p>
  <p class="notice">予約の必要はありません</p>
  <div class="doctor" role="img" aria-label="白衣を着た医師のイラスト"></div>

  <ul class="points">
    <li>インフルエンザに対する抵抗力がつくまで約2週間かかり、その効果は約5ヶ月間持続します。</li>
    <li>2回接種をご希望の方は、1回目接種から4週間後に2回目接種を行います。</li>
    <li>肺炎球菌ワクチンとの同時接種もできます。</li>
    <li>体温が37.5度以上、具合が悪い方は別の日に接種しましょう。</li>
    <li>当院では妊娠中の方も予防接種できます。</li>
  </ul>
  <div class="couple" role="img" aria-label="笑顔の高齢の夫婦のイラスト"></div>

  <table class="fees">
    <thead><tr><th>対象者</th><th>接種日</th><th>接種費用</th></tr></thead>
    <tbody>
      <tr>
        <td class="who">
          <span class="main">65歳以上</span>
          <span class="sub">60歳以上 65歳未満</span>
          <span class="tiny">心臓・腎臓・呼吸器の機能障害、<br>免疫の機能障害がある方</span>
        </td>
        <td>令和元年<br>10月11日<br>～<br>12月31日</td>
        <td>
          <span class="fee-city">緑ヶ丘市公費負担あり</span>
          <span class="fee-price">1,500<small>円</small></span>
          <span class="fee-count">(接種回数 1回)</span>
          <span class="fee-note">費用が免除になる方がいらっしゃいます</span>
        </td>
      </tr>
      <tr>
        <td class="who">
          <span class="other">上記以外の方</span>
          <span class="sub">13歳以上 65歳未満</span>
        </td>
        <td>令和元年<br>10月11日<br>～</td>
        <td>
          <div class="dose"><span>1回目</span>4,000円</div>
          <div class="dose second"><span>2回目</span>3,000円</div>
        </td>
      </tr>
    </tbody>
  </table>

  <footer class="clinic"><i></i>森下内科クリニック</footer>
</main>
</body>
</html>
```